Online trading school - Website design

We are building an online trading school (trading of shares, commodities, indices, currencies). The purpose is to teach online traders how to trade successfully. We need to design the homepage of the website and logo (bramwelloq.com will be the domain). The homepage will contain the following elements

- logo
- Sign in and Register links/buttons
- upper menu
- short introduction
- a couple of bullet points 'Why to join our school?'
- sign up form
- text
- bottom menu

Attached is a draft for the designer. The draft is just for an inspiration, the actual structure of the website can be different if the designer thinks so.

The designer is free to choose colors.

School

3 page

```html
<!DOCTYPE html>
<html lang="en">
<head>
<meta charset="utf-8">
<title>Trading School – Home</title>
<link rel="stylesheet" href="https://fonts.googleapis.com/css2?family=Arvo:wght@400;700&family=Open+Sans:wght@400;600;700&family=Roboto+Condensed:wght@300;400;700&family=Oswald:wght@500&display=swap">
<style>
  :root {
    --navy: #003a5c;
    --navy-deep: #02223a;
    --red: #c8102e;
    --orange: #f0700a;
    --ink: #333333;
    --text: #555555;
    --rule: #e2e2e2;
    --footer: #e3e3e3;
    --social: #b5b5b5;
    --white: #ffffff;
  }
  * { box-sizing: border-box; margin: 0; padding: 0; }
  html, body { width: 1047px; height: 1200px; overflow: hidden; background: var(--white); }
  body { position: relative; font-family: "Open Sans", Arial, sans-serif; color: var(--text); }

  .site-header { position: absolute; left: 0; top: 0; width: 1047px; height: 77px; border-bottom: 1px solid var(--rule); }
  .brand { position: absolute; left: 64px; top: 25px; font-family: "Oswald", "Arial Narrow", sans-serif; font-weight: 500; font-size: 22px; color: var(--ink); letter-spacing: -0.3px; }
  .account-btn { position: absolute; top: 24px; height: 31px; width: 80px; border: 2px solid; border-radius: 3px; font-family: "Open Sans", sans-serif; font-weight: 700; font-size: 11px; display: flex; align-items: center; justify-content: center; text-decoration: none; }
  .account-btn.sign-in { left: 816px; color: var(--red); border-color: var(--red); }
  .account-btn.register { left: 902px; color: var(--navy-deep); border-color: var(--navy-deep); }

  .main-nav { position: absolute; left: 0; top: 77px; width: 1047px; height: 43px; }
  .main-nav a { position: absolute; top: 6px; height: 32px; line-height: 32px; font-family: "Roboto Condensed", sans-serif; font-weight: 300; font-size: 16px; color: var(--ink); text-decoration: none; }
  .main-nav a.active { background: var(--red); color: var(--white); padding: 0 17px; border-radius: 3px; font-weight: 400; }
  .social { position: absolute; display: flex; gap: 4px; }
  .social span { width: 27px; height: 27px; border-radius: 50%; background: var(--social); }
  .main-nav .social { left: 892px; top: 8px; }

  .hero { position: absolute; left: 0; top: 120px; width: 1047px; height: 435px; background: linear-gradient(100deg, #5a4a3a 0%, #c7b8a6 30%, #8f8f93 52%, #2f4b7e 68%, #b9bfc4 85%, #6f7478 100%); }
  .welcome { position: absolute; left: 64px; top: 163px; width: 290px; height: 350px; }
  .welcome svg { position: absolute; left: 0; top: 0; }
  .welcome h1 { position: absolute; left: 0; top: 60px; width: 290px; text-align: center; font-family: "Arvo", serif; font-weight: 400; font-size: 23px; line-height: 23px; color: var(--navy); }
  .welcome .divider { position: absolute; left: 24px; top: 126px; width: 242px; height: 4px; border-top: 1px solid #c9bfa8; border-bottom: 1px solid #c9bfa8; }
  .welcome p { position: absolute; left: 20px; top: 154px; width: 250px; text-align: center; font-size: 13px; line-height: 22.5px; color: var(--text); }

  .join { position: absolute; top: 555px; height: 356px; width: 523px; }
  .join.why { left: 0; background: var(--navy); }
  .join.signup { left: 523px; width: 524px; background: var(--red); }
  .join h2 { position: absolute; top: 34px; width: 100%; text-align: center; font-family: "Arvo", serif; font-weight: 400; font-size: 24px; color: var(--white); }
  .join .accent { position: absolute; top: 74px; left: 50%; margin-left: -22px; width: 44px; height: 3px; border-radius: 2px; }
  .why .accent { background: #7fa3c0; }
  .signup .accent { background: #f08a9a; }

  .benefits { list-style: none; position: absolute; left: 91px; top: 102px; }
  .benefits li { width: 393px; height: 36px; margin-bottom: 8.5px; background: var(--navy-deep); border-radius: 18px; display: flex; align-items: center; padding-left: 9px; color: var(--white); font-weight: 600; font-size: 14.5px; }
  .benefits svg { margin-right: 11px; }

  .signup-form { position: absolute; left: 65px; top: 102px; width: 342px; }
  .signup-form .field { height: 35px; background: var(--white); border-radius: 2px; margin-bottom: 8.5px; padding-left: 11px; line-height: 35px; font-size: 13.5px; color: #666; }
  .signup-form .agree { display: flex; align-items: center; margin-top: 6px; font-size: 12.5px; color: var(--white); }
  .signup-form .agree i { width: 9px; height: 9px; background: var(--white); margin-right: 10px; display: inline-block; }
  .signup-form .submit { margin-top: 12px; height: 38px; background: var(--orange); border-radius: 2px; color: var(--white); font-weight: 700; font-size: 13px; display: flex; align-items: center; justify-content: center; }

  .offer { position: absolute; left: 64px; top: 944px; width: 920px; }
  .offer h2 { font-family: "Arvo", serif; font-weight: 400; font-size: 22px; color: var(--navy); }
  .offer p { margin-top: 12px; font-size: 13px; line-height: 22.5px; color: var(--text); }

  .site-footer { position: absolute; left: 0; top: 1154px; width: 1047px; height: 46px; background: var(--footer); }
  .site-footer .legal { position: absolute; left: 64px; top: 15px; font-size: 12.5px; color: var(--ink); }
  .site-footer .legal .sep { margin: 0 8px; }
  .site-footer .social { left: 890px; top: 9px; }
</style>
</head>
<body>
  <header class="site-header">
    <div class="brand">LOGO HERE</div>
    <a class="account-btn sign-in" href="#">SIGN IN</a>
    <a class="account-btn register" href="#">REGISTER</a>
  </header>

  <nav class="main-nav">
    <a class="active" href="#" style="left:64px">HOME</a>
    <a href="#" style="left:154px">ABOUT OUR SCHOOL</a>
    <a href="#" style="left:315px">RISK WARNING</a>
    <a href="#" style="left:442px">FAQ</a>
    <a href="#" style="left:502px">TRADING GLOSSARY</a>
    <a href="#" style="left:660px">CONTACT</a>
    <div class="social"><span></span><span></span><span></span></div>
  </nav>

  <section class="hero" role="img" aria-label="Photo of young pupils working at computers in a classroom"></section>

  <div class="welcome">
    <svg width="290" height="350" viewBox="0 0 290 350">
      <polygon points="0,30 145,3 290,30 290,322 145,347 0,322" fill="#ffffff"/>
      <polyline points="0,30 145,3 290,30" fill="none" stroke="#003a5c" stroke-width="6"/>
      <polyline points="0,322 145,347 290,322" fill="none" stroke="#003a5c" stroke-width="6"/>
      <rect x="0" y="27" width="16" height="8" fill="#003a5c"/>
      <rect x="274" y="27" width="16" height="8" fill="#003a5c"/>
      <rect x="0" y="317" width="16" height="8" fill="#003a5c"/>
      <rect x="274" y="317" width="16" height="8" fill="#003a5c"/>
    </svg>
    <h1>WELCOME TO<br>SCHOOL NAME</h1>
    <div class="divider"></div>
    <p>Lorem ipsum dolor sit amet, consectetur adipiscing elit, sed do eiusmod tempor incididunt ut labore et dolore magna aliqua. Ut enim ad minim veniam, quis nostrud exercitation ullamco laboris nisi ut aliquip ex ea commodo consequat.</p>
  </div>

  <section class="join why">
    <h2>WHY TO JOIN US?</h2>
    <div class="accent"></div>
    <ul class="benefits">
      <li><svg width="18" height="18" viewBox="0 0 18 18"><circle cx="9" cy="9" r="9" fill="#fff"/><path d="M5 9.2l2.7 2.7L13 6.6" fill="none" stroke="#02223a" stroke-width="2.2"/></svg>Best trading tips ever</li>
      <li><svg width="18" height="18" viewBox="0 0 18 18"><circle cx="9" cy="9" r="9" fill="#fff"/><path d="M5 9.2l2.7 2.7L13 6.6" fill="none" stroke="#02223a" stroke-width="2.2"/></svg>Secret tips from experts</li>
      <li><svg width="18" height="18" viewBox="0 0 18 18"><circle cx="9" cy="9" r="9" fill="#fff"/><path d="M5 9.2l2.7 2.7L13 6.6" fill="none" stroke="#02223a" stroke-width="2.2"/></svg>We teach you how to trade online</li>
      <li><svg width="18" height="18" viewBox="0 0 18 18"><circle cx="9" cy="9" r="9" fill="#fff"/><path d="M5 9.2l2.7 2.7L13 6.6" fill="none" stroke="#02223a" stroke-width="2.2"/></svg>Learn how to trade commodities</li>
      <li><svg width="18" height="18" viewBox="0 0 18 18"><circle cx="9" cy="9" r="9" fill="#fff"/><path d="M5 9.2l2.7 2.7L13 6.6" fill="none" stroke="#02223a" stroke-width="2.2"/></svg>Learn how to become a trader</li>
    </ul>
  </section>

  <section class="join signup">
    <h2>JOIN OUR SCHOOL NOW!</h2>
    <div class="accent"></div>
    <div class="signup-form">
      <div class="field">First name</div>
      <div class="field">Last name</div>
      <div class="field">Email</div>
      <div class="agree"><i></i>Agree with our tems and conditions</div>
      <div class="submit">SUBMIT</div>
    </div>
  </section>

  <section class="offer">
    <h2>WHAT DO WE OFFER?</h2>
    <p>Sed ut perspiciatis unde omnis iste natus error sit voluptatem accusantium doloremque laudantium, totam rem aperiam, eaque ipsa quae ab illo inventore veritatis et quasi architecto beatae vitae dicta sunt explicabo. Nemo enim ipsam voluptatem quia voluptas sit aspernatur aut odit aut fugit, sed quia consequuntur magni dolores eos qui ratione voluptatem sequi nesciunt. Neque porro quisquam est, qui dolorem ipsum quia dolor sit amet, consectetur, adipisci velit, sed quia non numquam eius modi tempora incidunt ut labore et dolore magnam aliquam quaerat voluptatem. Sed ut perspiciatis unde omnis iste natus error sit voluptatem accusantium doloremque laudantium, totam rem aperiam, eaque ipsa quae ab illo inventore veritatis et quasi architecto beatae vitae dicta sunt explicabo.</p>
  </section>

  <footer class="site-footer">
    <div class="legal">2016 © Steady Ledger Tutors.<span class="sep">|</span>Terms and Conditions<span class="sep">|</span>Privacy Protection</div>
    <div class="social"><span></span><span></span><span></span></div>
  </footer>
</body>
</html>
```